Square graphic for social media post

I want to create a 1080 x 1080px all-black image for the quote below that I can share on social media. I want the emphasis to be primarily on the quote, secondarily on the portrait, and third (smallest) on the logo. I want the background on the portrait to be edited so it's transparent and just shows the face of the person on a black background (no brick wall visible).

Graphic color: black
Text color: white
Content: "What we went through is going to make the greatest generation of hoteliers our industry has ever seen." << biggest text
Dorian Welk << smaller text
President, Marrowgate Hotels << smaller text
[image of person - use whichever version looks better to you]
[Add Lodging Ledger logo - whichever looks better to you]

This image needs to be readable when sized down much smaller (400x400?) so want the text and portrait to take up most of the space.

I'd like the output both as PNG and original file (preferably Canva). Thanks!

Target Market(s)

Hotel managers

Industry/Entity Type

Hospitality

Font styles to use
Sans Serif

Colors

Designer to choose colors to be used in the design.

Requirements
Must have
• Needs to focus on the quote and the person quoted (the portrait)

```html
<!DOCTYPE html>
<html lang="en">
<head>
<meta charset="utf-8">
<title>Quote Card – Dorian Welk</title>
<link rel="stylesheet" href="https://fonts.googleapis.com/css2?family=Bebas+Neue&family=Arimo:wght@400&display=swap">
<style>
  :root {
    --bg: #0b0909;
    --band: #1d1a1a;
    --band-line: #3a3434;
    --accent-line: #7a2a44;
    --text: #ffffff;
    --text-shadow: #8f8f8f;
    --rule: #d9d9d9;
    --portrait-a: #6d5a50;
    --portrait-b: #2b3f7a;
  }
  html, body {
    margin: 0;
    padding: 0;
    width: 1200px;
    height: 1200px;
    overflow: hidden;
    background: var(--bg);
  }
  .card {
    position: relative;
    width: 1200px;
    height: 1200px;
    background: var(--bg);
    overflow: hidden;
  }
  .backdrop {
    position: absolute;
    inset: 0;
  }
  .portrait {
    position: absolute;
    left: 0;
    top: 40px;
    width: 720px;
    height: 1160px;
    background:
      radial-gradient(ellipse 46% 40% at 48% 32%, #c9a58e 0%, #a07c68 45%, rgba(160,124,104,0) 75%),
      linear-gradient(180deg, rgba(0,0,0,0) 0%, rgba(0,0,0,0) 52%, var(--portrait-b) 68%, #1b2a57 100%),
      radial-gradient(ellipse 55% 60% at 48% 40%, var(--portrait-a) 0%, rgba(40,30,28,0.6) 60%, rgba(11,9,9,0) 85%);
    -webkit-mask-image: linear-gradient(90deg, #000 0%, #000 78%, transparent 100%);
            mask-image: linear-gradient(90deg, #000 0%, #000 78%, transparent 100%);
  }
  .quote {
    position: absolute;
    right: 56px;
    top: 70px;
    width: 500px;
    margin: 0;
    font-family: "Bebas Neue", "Oswald", sans-serif;
    font-weight: 400;
    color: var(--text);
    text-align: right;
    letter-spacing: 0.05em;
    text-shadow: 3px 4px 0 var(--text-shadow);
  }
  .quote span { display: block; line-height: 0.98; }
  .l1 { font-size: 76px; }
  .l2 { font-size: 82px; }
  .l3 { font-size: 96px; }
  .l4 { font-size: 96px; }
  .l5 { font-size: 108px; }
  .l6 { font-size: 72px; }
  .l7 { font-size: 76px; }
  .l8 { font-size: 80px; }
  .l9 { font-size: 100px; }
  .rule {
    position: absolute;
    left: 667px;
    top: 858px;
    width: 477px;
    height: 2px;
    background: var(--rule);
  }
  .attribution {
    position: absolute;
    right: 200px;
    top: 978px;
    font-family: "Arimo", "Helvetica", sans-serif;
    color: var(--text);
    text-align: right;
    line-height: 1.22;
  }
  .attribution .name { font-size: 28px; }
  .attribution .role,
  .attribution .company { font-size: 25px; }
  .publisher {
    position: absolute;
    left: 1018px;
    top: 960px;
    width: 120px;
    display: flex;
    flex-direction: column;
    align-items: center;
    gap: 12px;
    font-family: "Arimo", "Helvetica", sans-serif;
    font-size: 22px;
    line-height: 1.15;
    color: var(--text);
    text-align: center;
  }
  .publisher .dot {
    width: 44px;
    height: 44px;
    border-radius: 50%;
    background: var(--text);
  }
</style>
</head>
<body>
<div class="card">
  <svg class="backdrop" width="1200" height="1200" viewBox="0 0 1200 1200" aria-hidden="true">
    <polygon points="0,1200 0,1000 1200,0 1200,420 260,1200" fill="var(--band)"/>
    <g stroke="var(--band-line)" stroke-width="2">
      <line x1="0" y1="1040" x2="1200" y2="40"/>
      <line x1="0" y1="1100" x2="1200" y2="100"/>
      <line x1="40" y1="1200" x2="1200" y2="230"/>
      <line x1="150" y1="1200" x2="1200" y2="325"/>
    </g>
    <g stroke="var(--accent-line)" stroke-width="2">
      <line x1="760" y1="1200" x2="1200" y2="690"/>
      <line x1="800" y1="1200" x2="1200" y2="735"/>
      <line x1="840" y1="1200" x2="1200" y2="780"/>
      <line x1="880" y1="1200" x2="1200" y2="825"/>
      <line x1="920" y1="1200" x2="1200" y2="870"/>
      <line x1="960" y1="1200" x2="1200" y2="915"/>
    </g>
    <g stroke="#cfc7b8" stroke-width="2" opacity="0.6">
      <line x1="20" y1="290" x2="120" y2="190"/>
      <line x1="20" y1="310" x2="120" y2="210"/>
      <line x1="20" y1="330" x2="120" y2="230"/>
    </g>
  </svg>

  <div class="portrait" role="img" aria-label="Head-and-shoulders portrait of Dorian Welk, smiling, in a blue blazer and white open-collar shirt, on a black background"></div>

  <h1 class="quote">
    <span class="l1">What we went</span>
    <span class="l2">through is</span>
    <span class="l3">going to</span>
    <span class="l4">make the</span>
    <span class="l5">greatest</span>
    <span class="l6">generation of</span>
    <span class="l7">hoteliers our</span>
    <span class="l8">industry has</span>
    <span class="l9">ever seen</span>
  </h1>

  <div class="rule"></div>

  <div class="attribution">
    <div class="name">Dorian Welk</div>
    <div class="role">President</div>
    <div class="company">Marrowgate Hotels</div>
  </div>

  <div class="publisher">
    <span class="dot"></span>
    <span class="publisher-name">Lodging Ledger</span>
  </div>
</div>
</body>
</html>
```